Webdesign für Lindenhof
Zielgruppe
Lindenhof Brauckmann:
Zielgruppe sind alle, die gern Fisch essen. Es gibt einen Hofladen, einen Partyservice, eine Gaststätte und eine kleine Pension. Wichtig wäre darzustellen, dass es in der Gaststätte außer Fisch auch Fleisch gibt.
Einen Einblick geben Ihnen die Webseite und der beiliegende Flyer.
Aufgabenstellung
Die Öffnungszeiten von Gaststätte und Hofladen sollten prominent dargestellt werden. Neben den eigenen Bildern sollen auch stock-Fotos genutzt werden.

```html
<!DOCTYPE html>
<html lang="de">
<head>
<meta charset="utf-8">
<title>Lindenhof Brauckmann – Startseite</title>
<link rel="stylesheet" href="https://fonts.googleapis.com/css2?family=Source+Serif+4:wght@400;500&family=Overpass:wght@400;600&display=swap">
<style>
  :root {
    --paper: #fcfcfb;
    --ink: #4a3c2f;
    --ink-soft: #5b4d40;
    --earth: #594a3b;
    --earth-dark: #3b3028;
    --gold: #b08c5e;
    --cream: #f4efe6;
    --herb: rgba(200, 190, 175, 0.18);
    --herb-dark: rgba(176, 140, 94, 0.16);
  }
  * { box-sizing: border-box; margin: 0; padding: 0; }
  html, body { width: 1200px; height: 1200px; overflow: hidden; }
  body { background: var(--paper); font-family: "Overpass", Arial, sans-serif; color: var(--ink); }

  .intro {
    position: relative;
    height: 560px;
    background: var(--paper);
  }
  .intro__decor {
    position: absolute; left: 290px; top: 40px;
    width: 150px; height: 460px;
    border-radius: 75px;
    background: radial-gradient(ellipse at center, var(--herb), transparent 70%);
  }
  .intro__text {
    position: absolute; left: 120px; top: 120px; width: 500px;
    text-align: center;
  }
  .intro__title {
    font-family: "Source Serif 4", Georgia, serif;
    font-weight: 400; font-size: 48px; line-height: 1.12;
    color: var(--ink);
  }
  .intro__lead {
    margin: 34px auto 0; width: 420px;
    font-size: 13px; line-height: 1.55; color: var(--ink-soft);
  }
  .button {
    display: inline-block; margin-top: 40px;
    padding: 9px 30px 8px;
    background: var(--earth); color: var(--cream);
    border-radius: 22px;
    font-family: "Source Serif 4", Georgia, serif; font-size: 18px;
  }
  .intro__photo {
    position: absolute; left: 640px; top: 80px;
    width: 520px; height: 305px;
    background: linear-gradient(180deg, #6c7686 0%, #8a4a30 30%, #e6dcc6 50%, #a59b8c 75%, #5b6a3a 100%);
  }

  .events {
    position: relative;
    height: 640px;
    background: var(--earth);
    text-align: center;
    color: #fff;
  }
  .events__decor {
    position: absolute; top: 200px; width: 220px; height: 200px;
    background: radial-gradient(ellipse at center, var(--herb-dark), transparent 70%);
  }
  .events__decor--left { left: 160px; }
  .events__decor--right { right: 110px; }
  .events__title {
    padding-top: 80px;
    font-family: "Source Serif 4", Georgia, serif;
    font-weight: 400; font-size: 42px; line-height: 1.12;
  }
  .events__lead { margin-top: 22px; font-size: 13px; }
  .events__list {
    position: relative;
    width: 650px; margin: 44px auto 0;
    list-style: none;
  }
  .event { display: flex; gap: 7px; margin-bottom: 7px; height: 50px; }
  .event__date, .event__name {
    background: var(--earth-dark);
    display: flex; align-items: center;
    padding-left: 22px;
    font-size: 14px; font-weight: 600; text-align: left;
  }
  .event__date { width: 187px; }
  .event__name { flex: 1; }
  .event__mail {
    width: 48px; background: var(--gold);
    display: flex; align-items: center; justify-content: center;
  }
</style>
</head>
<body>
  <section class="intro">
    <div class="intro__decor" role="img" aria-label="Zarte Kräuterzeichnung als Hintergrund"></div>
    <div class="intro__text">
      <h1 class="intro__title">Der Lindenhof<br>Brauckmann</h1>
      <p class="intro__lead">Mit unserem Partyservice möchten wir dazu beitragen, dass Ihre Familienfeiern, Partys mit Freunden, Betriebsfeiern und Empfänge ein kulinarisches Erlebnis werden.</p>
      <a class="button">Mehr erfahren »</a>
    </div>
    <div class="intro__photo" role="img" aria-label="Foto der Gaststätte mit roter Holzveranda und gepflastertem Hof"></div>
  </section>

  <section class="events">
    <div class="events__decor events__decor--left" role="img" aria-label="Zarte Kräuterzeichnung"></div>
    <div class="events__decor events__decor--right" role="img" aria-label="Zarte Kräuterzeichnung"></div>
    <h2 class="events__title">Termine &amp;<br>Veranstaltungen</h2>
    <p class="events__lead">Wichtige Termine 2020/ 2021 zum vormerken und reservieren.</p>
    <ul class="events__list">
      <li class="event">
        <span class="event__date">Samstag, 21.08.2021</span>
        <span class="event__name">Cocktailabend ab 18 Uhr</span>
        <span class="event__mail">
          <svg width="18" height="14" viewBox="0 0 18 14"><rect x="0.75" y="0.75" width="16.5" height="12.5" fill="none" stroke="#fff" stroke-width="1.5"/><path d="M1 1 L9 8 L17 1 M1 13 L7 6.5 M17 13 L11 6.5" fill="none" stroke="#fff" stroke-width="1.5"/></svg>
        </span>
      </li>
      <li class="event">
        <span class="event__date">Sonntag, 26.09.2021</span>
        <span class="event__name">Schlemmerbuffet ab 11 Uhr bis 14 Uhr</span>
        <span class="event__mail">
          <svg width="18" height="14" viewBox="0 0 18 14"><rect x="0.75" y="0.75" width="16.5" height="12.5" fill="none" stroke="#fff" stroke-width="1.5"/><path d="M1 1 L9 8 L17 1 M1 13 L7 6.5 M17 13 L11 6.5" fill="none" stroke="#fff" stroke-width="1.5"/></svg>
        </span>
      </li>
    </ul>
  </section>
</body>
</html>
```